Visitenkarten-Design für Persisches Restaurant
Zielgruppe
persisches Restaurant, suche ein Hochwertiges Design für internationale Kunden
Aufgabenstellung
möchte eine hochwertige und elegante visitenkarte
auf der Vorderseite sollte das Logo sein und auf der Rückseite Öffnungszeit, Adresse, Tel. E-Mail und homepage

```html
<!DOCTYPE html>
<html lang="de">
<head>
<meta charset="utf-8">
<title>Narvani – Visitenkarte</title>
<link rel="stylesheet" href="https://fonts.googleapis.com/css2?family=Cinzel:wght@500&family=Barlow:wght@400;500&display=swap">
<style>
  :root {
    --backdrop: #d9d9d9;
    --card: #ffffff;
    --ink: #1e1e1e;
    --ink-soft: #6f6f6f;
    --rule: #9a9a9a;
  }
  * { box-sizing: border-box; margin: 0; padding: 0; }
  html, body {
    width: 1200px; height: 801px; overflow: hidden;
    background: var(--backdrop);
  }
  .sheet {
    position: relative; width: 1200px; height: 801px;
    display: flex; align-items: center; justify-content: center; gap: 60px;
  }
  .card {
    position: relative; width: 520px; height: 325px;
    background: var(--card);
    box-shadow: 0 2px 6px rgba(0,0,0,0.12);
  }
  /* Front */
  .card--front {
    display: flex; align-items: center; justify-content: center;
  }
  .wordmark { text-align: left; }
  .wordmark__name {
    display: flex; align-items: center; gap: 14px;
    font-family: "Cinzel", serif; font-weight: 500;
    font-size: 44px; letter-spacing: 2px; color: var(--ink);
  }
  .wordmark__dot {
    width: 18px; height: 18px; border-radius: 50%;
    background: var(--ink-soft);
  }
  .wordmark__tagline {
    margin-top: 4px; padding-left: 34px;
    font-family: "Barlow", sans-serif; font-weight: 400;
    font-size: 13px; letter-spacing: 3.6px; color: var(--ink-soft);
    text-transform: uppercase;
  }
  .wordmark__since {
    margin-left: 34px; margin-top: 3px; padding-top: 3px;
    border-top: 1px solid var(--rule);
    font-family: "Barlow", sans-serif; font-size: 9px;
    letter-spacing: 3px; color: var(--ink-soft); text-align: center;
    text-transform: uppercase;
  }
  /* Back */
  .card--back .back-name {
    position: absolute; left: 44px; top: 48px;
    display: flex; align-items: center; gap: 10px;
    font-family: "Cinzel", serif; font-weight: 500;
    font-size: 26px; letter-spacing: 1.5px; color: var(--ink);
  }
  .back-name .wordmark__dot { width: 12px; height: 12px; }
  .contact {
    position: absolute; left: 44px; bottom: 44px;
    list-style: none; display: flex; flex-direction: column; gap: 16px;
    font-family: "Barlow", sans-serif; font-size: 13px; color: var(--ink);
  }
  .contact__item { display: flex; align-items: flex-start; gap: 12px; line-height: 1.35; }
  .contact__icon { width: 14px; height: 14px; flex: none; margin-top: 2px; fill: var(--ink); }
</style>
</head>
<body>
<main class="sheet">
  <section class="card card--front" aria-label="Vorderseite">
    <div class="wordmark">
      <div class="wordmark__name"><span class="wordmark__dot"></span>NARVANI</div>
      <div class="wordmark__tagline">Persisches Restaurant</div>
      <div class="wordmark__since">Since 1999</div>
    </div>
  </section>

  <section class="card card--back" aria-label="Rückseite">
    <div class="back-name"><span class="wordmark__dot"></span>NARVANI</div>
    <ul class="contact">
      <li class="contact__item">
        <svg class="contact__icon" viewBox="0 0 24 24"><path d="M12 1a8 8 0 0 0-8 8c0 6 8 14 8 14s8-8 8-14a8 8 0 0 0-8-8zm0 11a3 3 0 1 1 0-6 3 3 0 0 1 0 6z"/></svg>
        <span>Eichenallee 9, 60316<br>Frankfurt am Main, Germany</span>
      </li>
      <li class="contact__item">
        <svg class="contact__icon" viewBox="0 0 24 24"><path d="M6.6 10.8a15 15 0 0 0 6.6 6.6l2.2-2.2a1 1 0 0 1 1-.25 11.4 11.4 0 0 0 3.6.57 1 1 0 0 1 1 1V20a1 1 0 0 1-1 1A17 17 0 0 1 3 4a1 1 0 0 1 1-1h3.5a1 1 0 0 1 1 1c0 1.25.2 2.45.57 3.57a1 1 0 0 1-.25 1z"/></svg>
        <span>+49 69 204815</span>
      </li>
      <li class="contact__item">
        <svg class="contact__icon" viewBox="0 0 24 24"><path d="M2 5h20v14H2z M2 5l10 8 10-8" fill="none" stroke="#1e1e1e" stroke-width="2"/></svg>
        <span>tischbote.de</span>
      </li>
    </ul>
  </section>
</main>
</body>
</html>
```